Personal Finance Author needs a postcard

Hi there,

I am a Canadian personal finance author and have published a new book called The Wealth Compass.

I teach Millennials how to create a 6-figure portfolio through investing (https://www.dariafelt.com/)

I'm speaking at some conferences so we were going to print some postcards to hand out to attendees with our info and calls-to-action on them.

I am looking for 4x6 (horizontal) postcard (no space needed for shipping label).

Logos, Headshots and Book Cover:
https://files.cloudvaultex.com/folders/8kQpZrT2mWvN4xLbJ7sHdYc3FgA9eUoRi?usp=sharing

Both sides will be full colour. I would like a clean and simple look. Our main sites are www.DariaFelt.com and www.TheWealthCompassBook.com if you want to get a sense of style and design.
I also uploaded a few marketing materials so you can see the existing designs.

Side 1:
Get Instant Access to your Free Resources - main headline

(small bullets underneath)
- The Wealth Compass Checklist
- Financial Worksheets
- Database of Investment Tools

DariaFelt.com/Resources

At the bottom, include "Don't forget to follow Daria Felt on social media:
ProNetwork: @dariafelt7
CircleFeed: @thewealthcompassbook PhotoLoop: @thewealthcompassbook ChirpLine: @WealthCompassBk"

Side 2:
Headline - Want to work directly with Daria and The Wealth Compass team to help you make your money grow and stay safe?

Work with us to (bullet point list)...
- Hire Daria as a Keynote Speaker
- Teach Financial Literacy Workshops
- Receive Financial Coaching

Want To Learn More About How We Can Help?
DariaFelt.com/Services

Include my contact info:
Daria Felt
Author | Speaker | Investor
daria@thewealthcompassbook.com
416-555-0187

Target Market(s)

Millennials who want to learn how to save and invest their money. I focus on stock market investing, real estate investing and entrepreneurship.

Industry/Entity Type

Financial Service

Font styles to use
Sans Serif

Colors

Designer to choose colors to be used in the design.

Requirements
Must have
• Photo of Daria Felt
• The Wealth Compass logo
• Green, Gold/Yellow to match existing colours
• modern business style postcard

```html
<!DOCTYPE html>
<html lang="en">
<head>
<meta charset="utf-8">
<title>The Wealth Compass – Postcard</title>
<link href="https://fonts.googleapis.com/css2?family=Roboto+Condensed:wght@400;700&family=Open+Sans:wght@600;700;800&display=swap" rel="stylesheet">
<style>
  :root{
    --green:#0b6b2b;
    --green-dark:#075220;
    --gold:#ecb12c;
    --gold-text:#e9a81f;
    --ink:#1c1c1c;
    --white:#ffffff;
    --backdrop:#8a8a8a;
    --photo-a:#d9d4cf;
    --photo-b:#3a3a3e;
  }
  *{box-sizing:border-box;margin:0;padding:0}
  html,body{width:1200px;height:1200px;overflow:hidden}
  body{background:var(--backdrop);position:relative;font-family:"Roboto Condensed",sans-serif;color:var(--ink)}
  .postcard{position:absolute;left:195px;width:810px;height:540px;background:var(--white);overflow:hidden;box-shadow:0 8px 24px rgba(0,0,0,.25)}
  .postcard--front{top:40px}
  .postcard--back{top:620px}
  .card-shapes{position:absolute;inset:0;width:100%;height:100%}

  /* front */
  .brand-mark{position:absolute;left:28px;top:24px;width:280px;font-weight:700;font-size:54px;line-height:.95;color:var(--green);text-transform:uppercase}
  .headshot{position:absolute;border-radius:4px}
  .headshot--front{left:60px;top:185px;width:270px;height:355px;background:linear-gradient(180deg,var(--photo-a) 0%,#c9b9aa 45%,var(--photo-b) 80%);border-radius:130px 130px 0 0}
  .resources{position:absolute;left:380px;top:22px;width:410px}
  .resources__kicker{font-weight:700;font-size:27px;color:var(--green);text-transform:uppercase;line-height:1}
  .resources__title{font-weight:700;font-size:50px;color:var(--gold-text);text-transform:uppercase;line-height:1;letter-spacing:-.5px}
  .resources__rule{width:44px;height:3px;background:var(--green);margin-top:6px}
  .resources__list{list-style:none;margin:26px 0 0 20px}
  .resources__list li{font-weight:700;font-size:20px;line-height:1.45;position:relative;padding-left:24px}
  .resources__list li::before{content:"";position:absolute;left:0;top:12px;width:6px;height:6px;border-radius:50%;background:var(--green)}
  .social{position:absolute;left:440px;top:302px;width:350px;color:var(--white)}
  .social__title{font-weight:700;font-size:21px;line-height:1.15}
  .social__title span{color:var(--gold)}
  .social__list{list-style:none;margin-top:10px}
  .social__list li{font-size:14.5px;line-height:1.45;display:flex;align-items:center;gap:7px}
  .social__list li::before{content:"";width:10px;height:10px;background:var(--gold);border-radius:2px;flex:none}
  .url-pill{position:absolute;left:440px;top:470px;width:280px;height:32px;border-radius:16px;background:var(--white);color:var(--ink);font-weight:700;font-size:16px;display:flex;align-items:center;justify-content:center}

  /* back */
  .pitch{position:absolute;left:30px;top:30px;width:400px;font-family:"Open Sans",sans-serif;font-weight:700;font-size:19px;line-height:1.25;color:var(--green)}
  .work-pill{position:absolute;left:60px;top:150px;width:340px;height:42px;border-radius:21px;background:var(--green);color:var(--white);font-family:"Open Sans",sans-serif;font-weight:800;font-size:24px;display:flex;align-items:center;justify-content:center;box-shadow:0 3px 0 var(--gold)}
  .services{list-style:none;position:absolute;left:45px;top:208px;width:420px;font-family:"Open Sans",sans-serif;font-weight:700;font-size:17px;line-height:1.4;color:#333}
  .services li{position:relative;padding-left:30px}
  .services li::before{content:"";position:absolute;left:0;top:10px;width:6px;height:6px;border-radius:50%;background:var(--green)}
  .learn-pill{position:absolute;left:45px;top:318px;width:400px;height:38px;border-radius:19px;background:var(--gold);color:var(--ink);font-family:"Open Sans",sans-serif;font-weight:700;font-size:14.5px;display:flex;align-items:center;justify-content:center}
  .contact{position:absolute;left:45px;top:378px;width:330px;color:var(--white);font-family:"Open Sans",sans-serif}
  .contact__url{font-weight:600;font-size:20px;padding-bottom:12px;border-bottom:1px dashed rgba(255,255,255,.7)}
  .contact__name{font-weight:800;font-size:26px;margin-top:10px;line-height:1.1}
  .contact__role{font-weight:600;font-size:13px}
  .contact__email{font-weight:600;font-size:13px;color:var(--gold)}
  .contact__phone{font-weight:800;font-size:30px;color:var(--gold);line-height:1.2}
  .headshot--round{left:395px;top:345px;width:170px;height:170px;border-radius:50%;border:4px solid var(--white);background:radial-gradient(circle at 50% 35%,#cdb8a5 0%,#ececec 40%,var(--photo-b) 85%)}
  .brand-mark--small{left:600px;top:22px;width:180px;font-size:36px;text-align:center}
  .book-cover{position:absolute;left:600px;top:140px;width:185px;height:330px;background:linear-gradient(160deg,#f3f1ea 0%,#e4e8dd 60%,var(--green) 100%);box-shadow:6px 6px 12px rgba(0,0,0,.3);border-left:10px solid #e0ddd3}
</style>
</head>
<body>

<section class="postcard postcard--front">
  <svg class="card-shapes" viewBox="0 0 810 540" aria-hidden="true">
    <path d="M285 540 C315 365 420 282 600 272 L810 255 L810 540 Z" fill="var(--gold)"/>
    <path d="M305 540 C335 385 430 300 605 292 L810 280 L810 540 Z" fill="var(--green)"/>
  </svg>
  <div class="brand-mark">The Wealth Compass</div>
  <div class="headshot headshot--front" role="img" aria-label="Headshot of Daria Felt in a dark blazer"></div>

  <div class="resources">
    <p class="resources__kicker">Get instant access to your</p>
    <h1 class="resources__title">Free Resources</h1>
    <div class="resources__rule"></div>
    <ul class="resources__list">
      <li>The Wealth Compass Checklist</li>
      <li>Financial Worksheets</li>
      <li>Database of Investment Tools</li>
    </ul>
  </div>

  <div class="social">
    <p class="social__title">Don't forget to follow <span>Daria Felt on social media</span></p>
    <ul class="social__list">
      <li>ProNetwork: @dariafelt7</li>
      <li>CircleFeed: @thewealthcompassbook</li>
      <li>PhotoLoop: @thewealthcompassbook</li>
      <li>ChirpLine: @WealthCompassBk</li>
    </ul>
  </div>
  <div class="url-pill">DariaFelt.com/Resources</div>
</section>

<section class="postcard postcard--back">
  <svg class="card-shapes" viewBox="0 0 810 540" aria-hidden="true">
    <path d="M420 540 C520 430 650 385 810 365 L810 540 Z" fill="var(--gold)"/>
    <path d="M0 345 C200 340 380 325 470 290 L540 540 L0 540 Z" fill="var(--green)"/>
    <path d="M370 0 C540 50 580 210 470 300" fill="none" stroke="var(--green)" stroke-width="26"/>
  </svg>

  <p class="pitch">Want to work directly with Daria and The Wealth Compass team to help you make your money grow and stay safe?</p>
  <div class="work-pill">Work with us to</div>
  <ul class="services">
    <li>Hire Daria as a Keynote Speaker</li>
    <li>Teach Financial Literacy Workshops</li>
    <li>Receive Financial Coaching</li>
  </ul>
  <div class="learn-pill">Want To Learn More About How We Can Help?</div>

  <div class="contact">
    <p class="contact__url">DariaFelt.com/Services</p>
    <p class="contact__name">Daria Felt</p>
    <p class="contact__role">Author | Speaker | Investor</p>
    <p class="contact__email">daria@thewealthcompassbook.com</p>
    <p class="contact__phone">416-555-0187</p>
  </div>

  <div class="headshot headshot--round" role="img" aria-label="Round portrait of Daria Felt smiling"></div>
  <div class="brand-mark brand-mark--small">The Wealth Compass</div>
  <div class="book-cover" role="img" aria-label="Cover of the book The Wealth Compass by Daria Felt, showing the author holding a calculator"></div>
</section>

</body>
</html>
```